Brookhaven Commerce Park Media Package

We are looking for a designer to unify our company's image throughout its stationery and marketing deliverables. We will be focusing on:
*Business Cards (3.5 x 2)
*Letter Head (Letter Size)
*PowerPoint Presentation Template,
*One Pager Flyer (Letter Size)
*Front of Elevator's bay: 4 photos of the elevator bays (two groups of 3 elevators) to which we are looking for designs for its doors and surrounding wall (vinyl prints)
*Font's suggestions
*Official color palette.
*Outdoor Street Signage: please use the following dimensions:
Sign #1 (Galloway Side): 48(W)x72"(H) (3 sided)
Sign #2: 24"(W)x48"(H) (3 sided)
Sign #3 (Top of Hill): 30(W)x54(H) (2 sides)
*Carport Sign:
See photos attached. The white letters will be removed, and a new sign will take place. Preferably, Cut-Out fonts, but we can consider an alternative approach for cost effective solution.
Find attached the approved logos.
______________________________________
We are a real estate holding company focused on the commercial office space in the Ohio, US, market.
You can check our site at www.brookhavenpark.example
As inspiration guidelines, we would like to see designs that are modern, minimalistic, dynamic and energetic.
Target Market(s)
General Population, Business Owners, Non-Profit Organizations, Government
Industry/Entity Type
Real Estate - Commercial Office Space - Flex Space

```html
<!DOCTYPE html>
<html lang="en">
<head>
<meta charset="utf-8">
<title>Brookhaven Plaza 41800 – Banner</title>
<link rel="stylesheet" href="https://fonts.googleapis.com/css2?family=Archivo+Black&display=swap">
<style>
  :root {
    --navy-deep: #070d18;
    --navy-mid: #0d1a2a;
    --teal-shade: #0f2a38;
    --gold: #d8b45c;
  }
  html, body {
    margin: 0;
    padding: 0;
    width: 1200px;
    height: 102px;
    overflow: hidden;
    background: var(--navy-deep);
  }
  .banner {
    position: relative;
    width: 1200px;
    height: 102px;
    overflow: hidden;
  }
  .banner-backdrop {
    position: absolute;
    inset: 0;
    background:
      radial-gradient(ellipse at 85% 40%, var(--teal-shade) 0%, transparent 55%),
      linear-gradient(100deg, var(--navy-deep) 0%, var(--navy-mid) 45%, var(--navy-deep) 75%, var(--teal-shade) 100%);
  }
  .brand-square {
    position: absolute;
    left: 176px;
    top: 23px;
    width: 56px;
    height: 56px;
    background: var(--gold);
  }
  .brand-name {
    position: absolute;
    left: 300px;
    top: 0;
    height: 102px;
    margin: 0;
    display: flex;
    align-items: center;
    font-family: "Archivo Black", "Arial Black", sans-serif;
    font-weight: 400;
    font-size: 50px;
    letter-spacing: 0.5px;
    line-height: 1;
    color: var(--gold);
    white-space: nowrap;
  }
</style>
</head>
<body>
  <header class="banner">
    <div class="banner-backdrop" role="img" aria-label="Dark navy and teal low-poly faceted background"></div>
    <div class="brand-square"></div>
    <h1 class="brand-name">BROOKHAVEN PLAZA 41800</h1>
  </header>
</body>
</html>
```